BRAVO Nutrition Mobile Application Layout

I am looking for professional grade app page layouts to use in my clickable prototype for an investor pitch.

B.R.A.V.O. is an acronym for Balanced Responsive Vitality Assessment Optimizer.

This app is a nutrition diet generation tool for the consumer (type in profile, diet is generated).

I am most interested in several pages consisting of:
- A landing/login page
- User profile page which will consist of a visual representation of adherence to the diet such as a pie chart, bar with percentage representing said adherence, etc.
- Profile settings page
- Blank general layout page (a standard template to be used with all pages in the application)

I would prefer greens, reds, and yellows in the design
The design should reflect health and nutrition
The design should have an "ease of use appearance"

Apps that are useful to look at are:
Trimwell Buddy
Nutrilogix
Grocevane

I have uploaded a "working" logo that I am using

I look forward to seeing your talents and appreciate your work in advance!

Target Market(s)

General population - health and wellness companies

Industry/Entity Type

Health And Wellness

Font styles to use
Serif
Sans Serif
Other font styles liked:
• Dealer's Choice

Colors
9ccb3b
f04a51
fbed22

Requirements
Must have
• - A landing/login page
• - User profile page which will consist of a visual representation of adherence to the diet such as a pie chart, bar with percentage representing said adherence, etc.
• - Profile settings page
• - Blank general layout page (a standard template to be used with all pages in the application)
• The design should reflect health and nutrition
• The design should have an "ease of use appearance"
Nice to have
• Incorporating the acronym spelled out.
• Common image in the background reflecting nutrition and health.

```html
<!DOCTYPE html>
<html lang="en">
<head>
<meta charset="utf-8">
<title>Settings</title>
<link href="https://fonts.googleapis.com/css2?family=Nunito+Sans:wght@400;600;700&display=swap" rel="stylesheet">
<style>
  :root {
    --header-bg: #ebedf0;
    --surface: #ffffff;
    --green: #9ccb3b;
    --green-icon: #8cc63f;
    --orange: #f08a3c;
    --yellow: #f3c300;
    --grey-icon: #8a8d90;
    --text: #2b2b2b;
    --chevron: #b9bcbf;
    --divider: #d9dbde;
    --logout: #e0552a;
  }
  * { margin: 0; padding: 0; box-sizing: border-box; }
  html, body { width: 675px; height: 1200px; overflow: hidden; background: var(--surface); }
  body { font-family: "Nunito Sans", Arial, sans-serif; color: var(--text); position: relative; }

  .header { position: absolute; left: 0; top: 0; width: 675px; height: 207px; background: var(--header-bg); }
  .status-bar { position: absolute; left: 0; top: 0; width: 675px; height: 36px; font-size: 21px; font-weight: 700; }
  .status-carrier { position: absolute; left: 10px; top: 6px; display: flex; align-items: center; gap: 6px; font-weight: 400; }
  .status-time { position: absolute; left: 0; right: 0; top: 6px; text-align: center; }
  .status-battery { position: absolute; right: 10px; top: 6px; display: flex; align-items: center; gap: 8px; font-weight: 400; }

  .menu-button { position: absolute; left: 22px; top: 58px; }
  .screen-title { position: absolute; left: 0; right: 0; top: 56px; text-align: center; font-size: 27px; font-weight: 600; }

  .settings-badge { position: absolute; left: 268px; top: 133px; width: 130px; height: 130px; border-radius: 50%; background: var(--surface); display: flex; align-items: center; justify-content: center; }
  .settings-badge-inner { width: 116px; height: 116px; border-radius: 50%; background: var(--green); display: flex; align-items: center; justify-content: center; }

  .settings-list { position: absolute; left: 0; top: 317px; width: 675px; list-style: none; }
  .settings-item { position: relative; height: 108px; margin-left: 27px; border-bottom: 2px solid var(--divider); display: flex; align-items: center; }
  .settings-item--last { height: 118px; padding-top: 6px; }
  .settings-icon { position: absolute; left: 6px; width: 36px; height: 36px; }
  .settings-label { position: absolute; left: 63px; font-size: 31px; font-weight: 400; }
  .settings-chevron { position: absolute; right: 22px; }

  .app-version { position: absolute; left: 0; right: 0; top: 963px; text-align: center; font-size: 27px; }
  .logout-bar { position: absolute; left: 0; top: 1093px; width: 675px; height: 107px; border-top: 2px solid var(--divider); border-bottom: 2px solid var(--divider); display: flex; align-items: center; justify-content: center; font-size: 25px; color: var(--logout); }
</style>
</head>
<body>
  <header class="header">
    <div class="status-bar">
      <div class="status-carrier">
        <svg width="34" height="16" viewBox="0 0 34 16"><rect x="0" y="11" width="5" height="5" fill="#000"/><rect x="7" y="8" width="5" height="8" fill="#000"/><rect x="14" y="5" width="5" height="11" fill="#000"/><rect x="21" y="2" width="5" height="14" fill="#000"/></svg>
        <span>Carrier</span>
        <svg width="26" height="18" viewBox="0 0 26 18"><path d="M13 17 L1 5 A17 17 0 0 1 25 5 Z" fill="#000"/></svg>
      </div>
      <div class="status-time">9:41 AM</div>
      <div class="status-battery">
        <svg width="12" height="20" viewBox="0 0 12 20"><path d="M1 5 L11 14 L6 19 L6 1 L11 6 L1 15" fill="none" stroke="#000" stroke-width="2"/></svg>
        <span>100%</span>
        <svg width="46" height="20" viewBox="0 0 46 20"><rect x="1" y="1" width="40" height="18" rx="4" fill="none" stroke="#000" stroke-width="2"/><rect x="4" y="4" width="34" height="12" rx="2" fill="#000"/><rect x="42" y="7" width="3" height="6" fill="#000"/></svg>
      </div>
    </div>
    <svg class="menu-button" width="42" height="30" viewBox="0 0 42 30" aria-label="Menu">
      <g stroke="var(--green)" stroke-width="4" stroke-linecap="round"><line x1="2" y1="3" x2="40" y2="3"/><line x1="2" y1="15" x2="40" y2="15"/><line x1="2" y1="27" x2="40" y2="27"/></g>
    </svg>
    <h1 class="screen-title">Settings</h1>
  </header>

  <div class="settings-badge">
    <div class="settings-badge-inner">
      <svg width="56" height="56" viewBox="0 0 56 56" aria-label="Settings">
        <g fill="none" stroke="#fff" stroke-width="3.5" stroke-linejoin="round">
          <path d="M24 4 h8 l1.5 7 a18 18 0 0 1 5 2.9 l6.8 -2.3 4 6.9 -5.3 4.8 a18 18 0 0 1 0 5.8 l5.3 4.8 -4 6.9 -6.8 -2.3 a18 18 0 0 1 -5 2.9 L32 52 h-8 l-1.5 -7 a18 18 0 0 1 -5 -2.9 l-6.8 2.3 -4 -6.9 5.3 -4.8 a18 18 0 0 1 0 -5.8 L6.7 22.1 l4 -6.9 6.8 2.3 a18 18 0 0 1 5 -2.9 Z"/>
          <circle cx="28" cy="28" r="8"/>
        </g>
      </svg>
    </div>
  </div>

  <ul class="settings-list">
    <li class="settings-item">
      <svg class="settings-icon" viewBox="0 0 36 36"><g fill="none" stroke="var(--orange)" stroke-width="2.6"><circle cx="18" cy="11" r="7"/><path d="M4 34 a14 14 0 0 1 28 0 Z"/></g></svg>
      <span class="settings-label">Account Details</span>
      <svg class="settings-chevron" width="14" height="26" viewBox="0 0 14 26"><path d="M2 2 L12 13 L2 24" fill="none" stroke="var(--chevron)" stroke-width="2.4"/></svg>
    </li>
    <li class="settings-item">
      <svg class="settings-icon" viewBox="0 0 36 36"><g fill="none" stroke="var(--yellow)" stroke-width="2.6"><path d="M3 4 h13 v6 a6.5 6.5 0 0 1 -13 0 Z"/><line x1="9.5" y1="17" x2="9.5" y2="31"/><line x1="4" y1="32" x2="15" y2="32"/><line x1="22" y1="4" x2="22" y2="12"/><line x1="27" y1="4" x2="27" y2="32"/><line x1="32" y1="4" x2="32" y2="12"/><path d="M22 12 a5 5 0 0 0 10 0"/></g></svg>
      <span class="settings-label">Adjust My Diet</span>
      <svg class="settings-chevron" width="14" height="26" viewBox="0 0 14 26"><path d="M2 2 L12 13 L2 24" fill="none" stroke="var(--chevron)" stroke-width="2.4"/></svg>
    </li>
    <li class="settings-item">
      <svg class="settings-icon" viewBox="0 0 36 36"><g fill="none" stroke="var(--green-icon)" stroke-width="2.6"><circle cx="18" cy="18" r="15"/><path d="M18 3 V18 H33"/></g></svg>
      <span class="settings-label">My Goals</span>
      <svg class="settings-chevron" width="14" height="26" viewBox="0 0 14 26"><path d="M2 2 L12 13 L2 24" fill="none" stroke="var(--chevron)" stroke-width="2.4"/></svg>
    </li>
    <li class="settings-item">
      <svg class="settings-icon" viewBox="0 0 36 36"><g fill="none" stroke="var(--grey-icon)" stroke-width="2.4" stroke-linejoin="round"><path d="M21 4 L32 15 L27 20 L22 30 L6 14 L16 9 Z"/><path d="M10 24 L5 29 a3 3 0 0 0 4 4 L13 28"/></g></svg>
      <span class="settings-label">Notification Settings</span>
      <svg class="settings-chevron" width="14" height="26" viewBox="0 0 14 26"><path d="M2 2 L12 13 L2 24" fill="none" stroke="var(--chevron)" stroke-width="2.4"/></svg>
    </li>
    <li class="settings-item settings-item--last">
      <svg class="settings-icon" viewBox="0 0 36 36"><g fill="none" stroke="var(--grey-icon)" stroke-width="2.2" stroke-linejoin="round"><path d="M6 2 H22 L30 10 V34 H6 Z"/><path d="M22 2 V10 H30"/><line x1="11" y1="16" x2="25" y2="16"/><line x1="11" y1="21" x2="25" y2="21"/><line x1="11" y1="26" x2="25" y2="26"/></g></svg>
      <span class="settings-label">Terms &amp; Conditions</span>
      <svg class="settings-chevron" width="14" height="26" viewBox="0 0 14 26"><path d="M2 2 L12 13 L2 24" fill="none" stroke="var(--chevron)" stroke-width="2.4"/></svg>
    </li>
  </ul>

  <p class="app-version">App version 1.0</p>
  <div class="logout-bar">Log Out</div>
</body>
</html>
```